Driving School needs brochure for clients charged before the courts with Road Rage

We are a driving school who provides courses to those charged with driving with road rage. This brochure which will be a pdf trifold will be emailed to lawyers, judges and clients. Needs to be extremely professional modern and classy.

Target Market(s)

judges, lawyers

Font styles to use
Serif
Sans Serif

Requirements
Must have
• Please replicate the current Savour the Lane brochure regarding the front page and graphic.
Final design will be a single pdf document with front page of trifold at top and inner at bottom. Should look similar in deign to Steady Mindful (brown brochure) brochure. Not same color. Final panel should be very similar/identical and same as middle panel on outside of trifold (top middle panel) i.e., contact information with phone number, email and website should be similar/identical.
Should not have
• any manufacturer name/logo or image that is obviously linked

```html
<!DOCTYPE html>
<html lang="en">
<head>
<meta charset="utf-8">
<title>Lanewise Driving Academy – Road Rage Trifold</title>
<link href="https://fonts.googleapis.com/css2?family=Oswald:wght@400;500&family=Open+Sans:wght@400;600&family=Montserrat:wght@400;500;600&display=swap" rel="stylesheet">
<style>
:root{
  --navy:#22376b;
  --ink:#1a1a1a;
  --black:#000;
  --white:#fff;
  --stage:#ffffff;
  --muted:#3b3b3b;
}
*{box-sizing:border-box;margin:0;padding:0}
html,body{width:669px;height:1200px;overflow:hidden;background:var(--stage)}
body{position:relative;font-family:"Open Sans",sans-serif;color:var(--ink)}
.spread{position:absolute;left:24px;width:621px;height:458px;display:flex;box-shadow:0 3px 8px rgba(0,0,0,.25);background:var(--white)}
.spread--outside{top:92px}
.spread--inside{top:612px}
.panel{position:relative;width:207px;height:458px;overflow:hidden}
.photo{position:absolute}
.url{font-family:"Open Sans",sans-serif;font-weight:600;font-size:6.4px;color:var(--navy)}

/* outside left */
.bg-block{position:absolute;left:0;top:0;width:207px;height:163px;background:var(--black)}
.bg-photo{left:10px;top:23px;width:185px;height:153px;background:linear-gradient(180deg,#b9d0e8 0%,#dfe6ea 28%,#8a8c8d 45%,#5c5d5f 100%)}
.background-copy{position:absolute;left:18px;top:196px;width:170px}
.section-title{font-family:"Montserrat",sans-serif;font-weight:600;font-size:8.6px;color:var(--navy);letter-spacing:.2px;padding-bottom:3px;border-bottom:1px solid var(--navy);width:110px;margin-bottom:9px}
.background-copy p{font-size:5.1px;line-height:7.4px;color:var(--muted);margin-bottom:7px}
.background .url{position:absolute;left:18px;top:422px}

/* outside middle */
.headline-cond{position:absolute;left:0;right:0;top:22px;text-align:center;font-family:"Oswald",sans-serif;font-weight:400;font-size:14.5px;line-height:19px;color:var(--ink);letter-spacing:-.2px}
.more-info{position:absolute;left:0;right:0;top:96px;text-align:center;font-family:"Montserrat",sans-serif;font-weight:600;font-size:10.5px;color:var(--navy)}
.more-info span{display:inline-block;border-bottom:1px solid var(--navy);padding-bottom:2px}
.contact-list{position:absolute;left:0;right:0;top:123px;list-style:none;text-align:center}
.contact-list li{height:33px;font-size:5.4px;font-weight:600}
.contact-list svg{display:block;margin:0 auto 3px}
.contact-band{position:absolute;left:0;bottom:0;width:207px;height:143px;background:var(--black)}
.contact-photo{left:11px;top:234px;width:185px;height:136px;border:1px solid var(--white);background:linear-gradient(135deg,#c8cdd4 0%,#6e7782 40%,#2b2f36 75%,#1c1f25 100%)}
.brand{text-align:center;position:absolute;left:0;right:0}
.brand-name{font-family:"Oswald",sans-serif;font-weight:500;font-size:7.4px;color:var(--navy);margin-bottom:2px}
.brand-tag{font-size:3.8px;line-height:1.35}
.brand-tag + .brand-tag{margin-top:3px}
.brand--dark{top:390px;color:var(--white)}
.brand--dark .brand-name{color:var(--white);font-size:6px}
.brand--light{top:26px;color:var(--navy)}

/* cover */
.cover-photo{left:0;top:0;width:207px;height:313px;background:linear-gradient(180deg,#c9d5ea 0%,#e8eef6 18%,#f2e7b2 34%,#e9c45e 46%,#8c6a2e 62%,#3a2d1e 80%,#201912 100%)}
.cover-box{position:absolute;left:31px;top:258px;width:176px;height:183px;background:var(--navy);color:var(--white)}
.cover-title{position:absolute;right:16px;top:33px;text-align:right;font-family:"Oswald",sans-serif;font-weight:500;font-size:18px;line-height:24px;letter-spacing:-.2px}
.cover-sub{position:absolute;left:0;right:0;top:87px;text-align:center;font-size:7.6px;line-height:11px}
.cover-rule{position:absolute;right:16px;top:126px;width:66px;height:1px;background:var(--white)}
.cover-box .url{position:absolute;left:0;right:0;top:145px;color:var(--white);text-align:center}

/* inside shared list */
.ticks{list-style:none}
.ticks li{position:relative;padding-left:7px;font-size:4.9px;line-height:7.4px;margin-bottom:5px}
.ticks li::before{content:"";position:absolute;left:0;top:2px;width:3.4px;height:3.4px;border:.6px solid currentColor;border-radius:50%}

/* inside left */
.topics{background:var(--navy);color:var(--white)}
.intro-block{position:absolute;left:18px;top:20px;width:172px}
.intro{font-family:"Montserrat",sans-serif;font-weight:500;font-size:6.2px;line-height:8.8px;margin-bottom:7px}
.topics-title{position:absolute;left:18px;top:99px;font-family:"Montserrat",sans-serif;font-weight:500;font-size:6.8px;border-bottom:1px solid var(--white);padding-bottom:2px}
.topic{position:absolute;left:50px;width:138px}
.topic--law{top:128px}
.topic--rage{top:204px}
.topic--body{top:316px}
.topic h3{font-family:"Montserrat",sans-serif;font-weight:600;font-size:6.6px;line-height:8.4px;margin-bottom:5px}
.topic-icon{position:absolute;left:-31px;top:22px}
.topics .url{color:var(--white);position:absolute;left:18px;top:424px;font-weight:400}

/* inside middle */
.strategy{position:absolute;left:44px;width:140px}
.strategy--manage{top:26px}
.strategy--context{top:157px}
.strategy--defensive{top:237px}
.strategy h3{font-family:"Montserrat",sans-serif;font-weight:600;font-size:6.6px;color:var(--navy);margin-bottom:6px}
.strategy .ticks{padding-left:2px}
.strategy .ticks li{color:var(--muted)}
.strategy-icon{position:absolute;left:-32px;top:26px;color:var(--navy)}
.strategy-band{position:absolute;left:0;bottom:0;width:207px;height:88px;background:var(--black)}
.strategy-photo{left:12px;top:334px;width:183px;height:107px;border:1px solid var(--white);background:linear-gradient(120deg,#7fa865 0%,#c9b28f 30%,#8a6b55 60%,#3c3a3a 100%)}

/* inside right */
.remote-band{position:absolute;left:0;top:0;width:207px;height:113px;background:var(--navy)}
.remote-card{position:absolute;left:11px;top:36px;width:183px;height:139px;border:1.5px solid var(--navy);border-radius:4px;background:linear-gradient(180deg,#ffffff 0%,#f1f3f7 100%)}
.remote-title{position:absolute;left:0;right:0;top:199px;text-align:center;font-family:"Montserrat",sans-serif;font-weight:500;font-size:15.5px;line-height:22px;color:var(--navy)}
.remote-offer{position:absolute;left:0;right:0;top:315px;text-align:center;font-family:"Montserrat",sans-serif;font-weight:600;font-size:21px;line-height:27px;color:var(--ink)}
.remote-rule{position:absolute;left:70px;top:385px;width:71px;height:2px;background:var(--navy)}
.remote .url{position:absolute;left:0;right:0;top:414px;text-align:center;color:var(--ink)}
</style>
</head>
<body>

<section class="spread spread--outside" aria-label="Trifold outside">
  <article class="panel background">
    <div class="bg-block"></div>
    <div class="photo bg-photo" role="img" aria-label="Photo of an empty desert highway with yellow centre lines"></div>
    <div class="background-copy">
      <h2 class="section-title">OUR BACKGROUND</h2>
      <p>Since its inception in 1998, Lanewise Driving Academy has strived to help drivers maintain their driving independence while leading safe and productive lives. Our promise of confident drivers on every mile drives our vision of helping drivers across industries and at all stages of our driving careers.</p>
      <p>Lanewise started out working with school boards to deliver driver training to beginner drivers. Thousands of students have graduated from our ministry-approved curriculum. We are also ministry-approved to instruct defensive driving (DDC) and driver improvement courses (DIC), for drivers with speeding tickets, de-merit points and at fault crashes.</p>
      <p>Lanewise has also evolved to provide comprehensive driver re-habilitation to those who have lost, or are at risk of losing their license for medical reasons. This includes mobility issues requiring adaptive equipment, as well as traumatic crashes resulting in cognitive impairments and PTSD. We work with clients before the courts charged with impaired driving (alcohol, cannabis, opioids), road rage and stunt driving.</p>
      <p>Founder Daniel Hartley started driving at an early age on his parent’s farm. Driving professionally and doing so safely is in his DNA. Daniel has a degree in Business and Psychology and is a certified in-car and in-class driving instructor.</p>
    </div>
    <span class="url">www.lanewisedriving.ca</span>
  </article>

  <article class="panel contact">
    <h2 class="headline-cond">MAINTAINING DRIVING<br>INDEPENDENCE WHILE LEADING<br>SAFE AND PRODUCTIVE LIVES</h2>
    <p class="more-info"><span>For more information</span></p>
    <ul class="contact-list">
      <li><svg width="9" height="9" viewBox="0 0 10 10"><circle cx="5" cy="5" r="5" fill="#22376b"/><path d="M3.3 2.6l1 1-.5.7c.4.8 1 1.4 1.8 1.8l.7-.5 1 1-.7.8c-1.9-.4-3.6-2.1-4-4z" fill="#fff"/></svg>555-210-4477</li>
      <li><svg width="9" height="9" viewBox="0 0 10 10"><circle cx="5" cy="5" r="5" fill="#22376b"/><rect x="2.6" y="3.3" width="4.8" height="3.4" fill="#fff"/><path d="M2.6 3.3L5 5.2l2.4-1.9" stroke="#22376b" stroke-width=".5" fill="none"/></svg>info@lanewisedriving.ca</li>
      <li><svg width="9" height="9" viewBox="0 0 10 10"><circle cx="5" cy="5" r="5" fill="#22376b"/><circle cx="5" cy="5" r="2.6" stroke="#fff" stroke-width=".6" fill="none"/><path d="M2.4 5h5.2M5 2.4c-1.3 1.5-1.3 3.7 0 5.2M5 2.4c1.3 1.5 1.3 3.7 0 5.2" stroke="#fff" stroke-width=".5" fill="none"/></svg>www.lanewisedriving.ca</li>
    </ul>
    <div class="contact-band"></div>
    <div class="photo contact-photo" role="img" aria-label="Photo of a driver's hands on a steering wheel"></div>
    <div class="brand brand--dark">
      <div class="brand-name">Lanewise Driving Academy</div>
      <p class="brand-tag">Confident drivers, every mile</p>
      <p class="brand-tag">Licensing help at every stage<br>Novice, Recovery &amp; Refresher</p>
    </div>
  </article>

  <article class="panel cover">
    <div class="photo cover-photo" role="img" aria-label="Photo of a driver at the wheel heading into a sunlit field road"></div>
    <div class="brand brand--light">
      <div class="brand-name">Lanewise Driving Academy</div>
      <p class="brand-tag">Confident drivers, every mile</p>
      <p class="brand-tag">Licensing help at every stage<br>Novice, Recovery &amp; Refresher</p>
    </div>
    <div class="cover-box">
      <h1 class="cover-title">ROAD RAGE<br>SAVOUR THE LANE</h1>
      <p class="cover-sub">A 1-day educational course for<br>those charged with RoadRage</p>
      <span class="cover-rule"></span>
      <span class="url">www.lanewisedriving.ca</span>
    </div>
  </article>
</section>

<section class="spread spread--inside" aria-label="Trifold inside">
  <article class="panel topics">
    <div class="intro-block">
      <p class="intro">A 1-day, 7-hour, intensive remedial measures course for those charged with road rage</p>
      <p class="intro">Our goal is to equip our customers with knowledge and to help them avoid something devastating and/or irreversible from happening in the future</p>
    </div>
    <h2 class="topics-title">Topics covered</h2>
    <div class="topic topic--law">
      <svg class="topic-icon" width="16" height="16" viewBox="0 0 16 16"><circle cx="8" cy="8" r="6.5" fill="none" stroke="#fff" stroke-width=".8"/></svg>
      <h3>Law</h3>
      <ul class="ticks">
        <li>Highway Traffic Act (privilege vs right</li>
        <li>Federal and Provincial</li>
        <li>Implications of criminal record (financial, work relationships, etc</li>
      </ul>
    </div>
    <div class="topic topic--rage">
      <svg class="topic-icon" width="16" height="16" viewBox="0 0 16 16"><circle cx="8" cy="8" r="6.5" fill="none" stroke="#fff" stroke-width=".8"/></svg>
      <h3>Road Rage</h3>
      <ul class="ticks">
        <li>Triggers</li>
        <li>Personality types (Type A); Holmes &amp; Rahe stress scale</li>
        <li>Aggressive driving (overlap between aggressors (and victims</li>
        <li>Psychiatric issues/PTSD: Not uncommon to have professional drivers come through the course due to over-exposure to stress from driving (both on (the job or the commute to their driving job</li>
      </ul>
    </div>
    <div class="topic topic--body">
      <svg class="topic-icon" width="16" height="16" viewBox="0 0 16 16"><circle cx="8" cy="8" r="6.5" fill="none" stroke="#fff" stroke-width=".8"/></svg>
      <h3>Physiology and the negative<br>impacts of stress on the body</h3>
      <ul class="ticks">
        <li>Fight or flight response: how it works</li>
        <li>Hormones (Adrenaline, Cortisol, etc Chronic levels of exposure/Immune system suppression, hypertension</li>
        <li>Substances (will do brief overview of drinking and driving if relevant i.e., individual risk factors and (thresholds</li>
      </ul>
    </div>
    <span class="url">www.lanewisedriving.ca</span>
  </article>

  <article class="panel strategies">
    <div class="strategy strategy--manage">
      <svg class="strategy-icon" width="16" height="16" viewBox="0 0 16 16"><circle cx="8" cy="8" r="6.5" fill="none" stroke="currentColor" stroke-width=".8"/></svg>
      <h3>Strategies to manage</h3>
      <ul class="ticks">
        <li>Window of tolerance (hyper-arousal vs hy-po-arousal</li>
        <li>Breathing: how to have the cerebral part of the brain making decisions and not “lizard” part of brain</li>
        <li>We look at how our bodies have not kept up from an evolutionary point of view to manage daily stresses and stimuli</li>
        <li>Our habits: approx.. 50% of our decisions are made with little to no decision-making process; stages of change theory</li>
      </ul>
    </div>
    <div class="strategy strategy--context">
      <svg class="strategy-icon" width="16" height="16" viewBox="0 0 16 16"><circle cx="8" cy="8" r="6.5" fill="none" stroke="currentColor" stroke-width=".8"/></svg>
      <h3>Personal context</h3>
      <ul class="ticks">
        <li>Genetics&amp; socialization (role models&amp;predis positions</li>
        <li>Analysis of triggers leading up to event; what is really causing it, e.g., sometimes it can be systemic such as our commute</li>
      </ul>
    </div>
    <div class="strategy strategy--defensive">
      <svg class="strategy-icon" width="16" height="16" viewBox="0 0 16 16"><circle cx="8" cy="8" r="6.5" fill="none" stroke="currentColor" stroke-width=".8"/></svg>
      <h3>Defensive Driving skills</h3>
      <ul class="ticks">
        <li>The golden rule: Following distance</li>
        <li>Defensive stopping (what we should do every time we apply brakes</li>
        <li>Using your eyes and strategic driving</li>
        <li>Driving in adverse conditions-they exist every time we drive (human, environmental, machine</li>
      </ul>
    </div>
    <div class="strategy-band"></div>
    <div class="photo strategy-photo" role="img" aria-label="Photo of a driving student at the wheel with an instructor beside her"></div>
  </article>

  <article class="panel remote">
    <div class="remote-band"></div>
    <div class="remote-card" role="img" aria-label="Illustration of an online lesson with an instructor at a board and floating video, play and course icons"></div>
    <h2 class="remote-title">COURSES ARE<br>INDIVIDUALLY<br>TAILORED<br>ONE-ON-ONE</h2>
    <p class="remote-offer">OFFERED<br>REMOTELY!</p>
    <span class="remote-rule"></span>
    <span class="url">www.lanewisedriving.ca</span>
  </article>
</section>

</body>
</html>
```